Classical Chamber Choir needs an electronic and printable flyer for an Easter Concert

I am the new Artistic Director of the Halvane Chorale. We would like to advertise our upcoming concert on April 5 and are seeking a new, more youthful, contemporary look for the choir's advertising. Previously they have used classical curly letters and dark colours. Perhaps black/grey and white would work?
The choir is 27 years old and has many loyal and some quite elderly singers. We would now like to extend our appeal to the younger singers who are in the choir - age group 35 - 60 and we are keen to attract more in the 30/40 age group. I would like something contemporary in feel, uncluttered, minimalist and artistically appealing. More Morwelt than Pilard - more Fenzarotti than Drecklin. Some inspiration starters: Valdurro line drawings, linocut designs, Emil Vortanek pencil drawings. I am hoping these references might inspire you. Here are some other ideas using line from Gyula Fenyvesi:
https://pics.vistrel.example/qw7RtPz2LmNbXcYhA
https://pics.vistrel.example/Hs3KdVn8WpJtRfZ4M
We would require an A4 flyer, (high res. and low res.) DL, jpg for Chatterly and a 10cm. size to put on the front of the Concert Programme.

```html
<!DOCTYPE html>
<html lang="en">
<head>
<meta charset="utf-8">
<title>Halvane Chorale – Easter Concert Flyer</title>
<link rel="stylesheet" href="https://fonts.googleapis.com/css2?family=Roboto+Condensed:wght@300;400&family=Michroma&family=Questrial&display=swap">
<style>
  :root {
    --page-bg: #d6d6d6;
    --flyer-bg: #0b0b0c;
    --ink-white: #f4f4f4;
    --ink-soft: #cfcfd4;
    --accent-orange: #d9852a;
    --score-tone: #2a2a2a;
    --keys-light: #c9c4e6;
    --keys-dark: #4b4578;
  }
  * { box-sizing: border-box; margin: 0; padding: 0; }
  html, body {
    width: 1200px; height: 1200px; overflow: hidden;
    background: var(--page-bg);
  }
  .flyer {
    position: absolute; left: 204px; top: 40px;
    width: 792px; height: 1120px;
    background: var(--flyer-bg);
    overflow: hidden;
    font-family: "Roboto Condensed", sans-serif;
    color: var(--ink-white);
    text-align: center;
  }
  .score-art {
    position: absolute; left: 0; top: 0; width: 100%; height: 600px;
    background: radial-gradient(ellipse at 30% 35%, var(--score-tone) 0%, #161616 45%, var(--flyer-bg) 85%);
  }
  .keyboard-art {
    position: absolute; left: 0; top: 640px; width: 100%; height: 340px;
    background: linear-gradient(180deg, #0b0b0c 0%, var(--keys-dark) 30%, var(--keys-light) 60%, #5a5488 85%, #0b0b0c 100%);
  }
  .content { position: relative; z-index: 1; }
  .presenter {
    padding-top: 70px;
    font-weight: 300; font-size: 60px; letter-spacing: 1px; line-height: 1;
  }
  .present-word {
    font-family: "Questrial", sans-serif;
    font-size: 22px; letter-spacing: 12px; margin-top: 8px;
  }
  .divider { display: block; margin: 6px auto 0; }
  .headline {
    color: var(--accent-orange); font-weight: 400;
    font-size: 42px; line-height: 1.1; margin-top: 14px;
  }
  .company-line { font-size: 28px; letter-spacing: 2px; margin-top: 10px; }
  .masters {
    font-family: "Michroma", sans-serif;
    font-size: 40px; letter-spacing: 6px; line-height: 1.2;
  }
  .composers { font-size: 27px; margin-top: 2px; }
  .date-line {
    color: var(--accent-orange); font-weight: 300;
    font-size: 66px; margin-top: 16px; line-height: 1.1;
  }
  .date-line sup { font-size: 30px; vertical-align: 26px; }
  .venue { font-size: 38px; letter-spacing: 3px; line-height: 1.15; margin-top: 10px; }
  .performers {
    font-family: "Questrial", sans-serif; color: var(--ink-soft);
    font-size: 16px; line-height: 1.55; margin-top: 34px;
  }
  .director { font-family: "Questrial", sans-serif; font-size: 23px; margin-top: 6px; }
  .programmes {
    position: absolute; right: 44px; top: 960px; z-index: 1;
    font-family: "Questrial", sans-serif; text-align: right;
  }
  .programmes .label { font-size: 17px; letter-spacing: 3px; color: var(--ink-soft); }
  .programmes .value { font-size: 26px; }
  .tickets {
    position: absolute; left: 0; right: 0; top: 1040px; z-index: 1;
    font-family: "Questrial", sans-serif;
  }
  .tickets .label { font-size: 24px; letter-spacing: 4px; color: var(--ink-soft); }
  .tickets .value { font-size: 19px; margin-top: 4px; }
</style>
</head>
<body>
  <main class="flyer">
    <div class="score-art" role="img" aria-label="Faint handwritten sheet music manuscript in dark grey tones"></div>
    <div class="keyboard-art" role="img" aria-label="Photograph of piano keys lit in soft lavender light"></div>

    <div class="content">
      <h1 class="presenter">HALVANE CHORALE</h1>
      <p class="present-word">PRESENT</p>
      <svg class="divider" width="240" height="16" viewBox="0 0 240 16" aria-hidden="true">
        <line x1="0" y1="13" x2="240" y2="13" stroke="var(--accent-orange)" stroke-width="1"/>
        <polygon points="120,1 122,6 127,6 123,9 125,14 120,11 115,14 117,9 113,6 118,6" fill="var(--accent-orange)"/>
      </svg>
      <h2 class="headline">KESSNER AT EASTER<br>KESSNER STABAT MATER OP. 47</h2>
      <p class="company-line">IN THE COMPANY OF THE</p>
      <p class="masters">RUSSIAN MASTERS</p>
      <p class="composers">VOROBYANIN, TARASYUK, BELOZEROV, KAMYSHEV</p>
      <p class="date-line">5<sup>TH</sup> APRIL, 2020 - 5 PM</p>
      <p class="venue">ST. ALDRIC CHURCH<br>CALLOWAY STREET FERNDALE HILL</p>
      <p class="performers">
        Soloists - Lena Whitcombe, Alistair Crane, Gordon Carrow<br>
        String Quartet - Yevgeni Sorel, Marla Pheng, Rowan Hallett, Tamás Szerdi<br>
        Organ - Josefina Arden
      </p>
      <p class="director">Artistic Director Ilka Dravenholt</p>
    </div>

    <div class="programmes">
      <p class="label">PROGRAMMES</p>
      <p class="value">Gold Coin Donation</p>
    </div>

    <div class="tickets">
      <p class="label">TICKETS</p>
      <p class="value">$30/ $25/ $10 Student --- Children under 12 free</p>
    </div>
  </main>
</body>
</html>
```